Need Letterhead Design & Matching Business Card

I have a logo that I love already. But the letterhead is less than appealing and boring. I'd like a design for my letterhead which I will match with business cards. Also, I'd like to have used fonts that are generally available, as my current letterhead uses a font named "SPACE" which nobody has unless they download it...so when a Word version is forwarded, it looks awful on the receiver's screed due to not having the font. That being said, modern is the look we like and are going for.

My business is "Halloran Brightmoor PC" - a law firm specializing in representing people who have suffered catastrophic injuries or death (plane, auto, train crashes etc.).

See attached letterhead, which has all of the pertinent information. My logo is also attached in various formats.

```html
<!DOCTYPE html>
<html lang="en">
<head>
<meta charset="utf-8">
<title>Halloran Brightmoor PC – Stationery</title>
<link href="https://fonts.googleapis.com/css2?family=Questrial&family=Lato:wght@400&display=swap" rel="stylesheet">
<style>
  :root {
    --backdrop: #d4d4d6;
    --paper: #ffffff;
    --ink: #111111;
    --body-grey: #8a8a8a;
    --on-dark: #ffffff;
  }
  * { box-sizing: border-box; margin: 0; padding: 0; }
  html, body { width: 1194px; height: 1200px; overflow: hidden; }
  body { background: var(--backdrop); position: relative; font-family: "Questrial", sans-serif; color: var(--ink); }

  .sheet { position: absolute; background: var(--paper); overflow: hidden; }

  .brand { display: flex; align-items: center; justify-content: center; gap: 8px; letter-spacing: 0.5px; text-transform: uppercase; font-family: "Questrial", sans-serif; white-space: nowrap; }
  .brand-square { background: var(--ink); flex: none; }
  .brand--light { color: var(--on-dark); }
  .brand--light .brand-square { background: var(--on-dark); }

  .band { position: absolute; left: 0; right: 0; bottom: 0; background: var(--ink); color: var(--on-dark); font-family: "Questrial", sans-serif; text-transform: uppercase; letter-spacing: 0.6px; }
  .band svg { fill: none; stroke: var(--on-dark); stroke-width: 1.4; flex: none; }
  .contact-line { display: flex; align-items: center; gap: 6px; }

  /* Letterhead */
  .letterhead { left: 84px; top: 62px; width: 586px; height: 759px; }
  .letterhead .brand { position: absolute; top: 34px; left: 0; right: 0; font-size: 20px; }
  .letterhead .brand-square { width: 36px; height: 36px; }
  .salutation { position: absolute; left: 49px; top: 238px; font-family: "Lato", sans-serif; font-size: 11px; color: var(--body-grey); }
  .letter-body { position: absolute; left: 37px; top: 286px; width: 513px; font-family: "Lato", sans-serif; font-size: 10.6px; line-height: 13.9px; color: var(--body-grey); text-align: justify; }
  .letter-body p + p { margin-top: 13.9px; }
  .letter-body p:first-child { text-indent: 34px; }
  .letterhead .band { height: 60px; font-size: 7.2px; padding: 0 37px; display: flex; justify-content: space-between; align-items: center; }
  .band-address { display: flex; align-items: center; gap: 8px; line-height: 10px; }
  .band-contacts { line-height: 9.2px; }

  /* Business cards */
  .card { width: 283px; height: 161px; }
  .card-front { left: 789px; top: 254px; }
  .card-front .brand { position: absolute; top: 22px; left: 0; right: 0; font-size: 15px; gap: 6px; }
  .card-front .brand-square { width: 30px; height: 30px; }
  .card-person { position: absolute; top: 77px; left: 0; right: 0; text-align: center; }
  .card-name { font-size: 10.5px; letter-spacing: 1.2px; text-transform: uppercase; }
  .card-title { font-size: 6px; letter-spacing: 0.8px; margin-top: 3px; text-transform: uppercase; }
  .card-front .band { height: 40px; font-size: 4.6px; padding: 0 13px; display: flex; justify-content: space-between; align-items: center; line-height: 5.6px; }
  .card-front .band svg { width: 5px; height: 5px; }
  .card-back { left: 790px; top: 436px; background: var(--ink); }
  .card-back .brand { position: absolute; top: 65px; left: 0; right: 0; font-size: 15px; gap: 6px; }
  .card-back .brand-square { width: 30px; height: 30px; }

  /* Envelope */
  .envelope { left: 84px; top: 872px; width: 620px; height: 276px; }
  .envelope .brand { position: absolute; top: 34px; left: 0; right: 0; font-size: 20px; }
  .envelope .brand-square { width: 42px; height: 42px; }
  .envelope .band { height: 35px; font-size: 7.2px; display: flex; justify-content: center; align-items: center; }
</style>
</head>
<body>

<section class="sheet letterhead" aria-label="Letterhead">
  <div class="brand"><span class="brand-square"></span><span>Halloran Brightmoor PC</span></div>
  <p class="salutation">Dear Sir</p>
  <div class="letter-body">
    <p>Lorem ipsum dolor sit amet, consectetur adipiscing elit. Integer eu odio mattis, pulvinar turpis quis, faucibus nisl. Proin feugiat, erat vitae cursus pharetra, enim est semper ligula, in malesuada orci nisl et diam. Etiam elementum metus ac fringilla vulputate. Etiam mattis ligula sed ante mollis bibendum. Orci varius natoque penatibus et magnis dis parturient montes, nascetur ridiculus mus.</p>
    <p>Ut nibh augue, blandit ac orci ac, rutrum congue enim. Suspendisse gravida vulputate felis, quis interdum orci tincidunt quis. Praesent imperdiet maximus neque. Mauris ut dui enim. Nullam at efficitur elit. Donec ante ipsum, fermentum at lectus vel, blandit vulputate ante. Proin luctus suscipit diam id vestibulum. Morbi malesuada id mauris eget ullamcorper.</p>
    <p>Donec varius orci purus, vitae aliquam libero volutpat id. Integer sed imperdiet libero. Aliquam accumsan, risus sit amet ornare consectetur, turpis felis dictum justo, non rhoncus mauris dui sed velit. Pellentesque habitant morbi tristique senectus et netus et malesuada fames ac turpis egestas. Pellentesque tincidunt vitae ligula nec imperdiet. Donec sed congue enim. Nullam elementum faucibus nulla nec vestibulum. Sed at tempor ligula. In quis vulputate nunc. Integer at gravida lacus, ac tristique risus. Sed at vulputate nulla.</p>
    <p>Praesent blandit nunc eu efficitur commodo. In tempor nisi ex, vel venenatis ante vestibulum a. Duis vestibulum nibh a erat sagittis, nec euismod lorem varius. Nam ultricies turpis sed justo sollicitudin volutpat. Morbi sed mollis eros. Sed quis tortor id enim vehicula porttitor. Curabitur non aliquam ex. Phasellus dignissim fermentum elit, at finibus ligula mattis eget.</p>
  </div>
  <footer class="band">
    <div class="band-address">
      <svg width="8" height="11" viewBox="0 0 8 11"><path d="M4 10.3 C1.6 7 .8 5.6 .8 4 A3.2 3.2 0 0 1 7.2 4 C7.2 5.6 6.4 7 4 10.3Z"/><circle cx="4" cy="4" r="1.1"/></svg>
      <div>4820 Larkspur Ave. | Suite 600<br>Fairhaven, CA 90418</div>
    </div>
    <div class="band-contacts">
      <div class="contact-line"><svg width="7" height="7" viewBox="0 0 8 8"><rect x=".7" y="1.5" width="6.6" height="5"/><path d="M.7 1.5 4 4.4 7.3 1.5"/></svg>dmercer@halloranbrightmoor.com</div>
      <div class="contact-line"><svg width="7" height="7" viewBox="0 0 8 8"><circle cx="4" cy="4" r="3.3"/><path d="M.7 4h6.6M4 .7c-1.8 2-1.8 4.6 0 6.6M4 .7c1.8 2 1.8 4.6 0 6.6"/></svg>www.halloranbrightmoor.com</div>
      <div class="contact-line"><svg width="7" height="7" viewBox="0 0 8 8"><path d="M1.2 1.2 2.8.9 3.6 2.6 2.7 3.4C3.2 4.4 3.8 5 4.7 5.4L5.5 4.5 7.1 5.3 6.8 6.9C3.8 7 1 4.3 1.2 1.2Z"/></svg>Tel: (855) 555-0147</div>
    </div>
  </footer>
</section>

<section class="sheet card card-front" aria-label="Business card front">
  <div class="brand"><span class="brand-square"></span><span>Halloran Brightmoor PC</span></div>
  <div class="card-person">
    <div class="card-name">R. Daniel Mercer</div>
    <div class="card-title">President</div>
  </div>
  <footer class="band">
    <div class="contact-line"><svg viewBox="0 0 8 11"><path d="M4 10.3 C1.6 7 .8 5.6 .8 4 A3.2 3.2 0 0 1 7.2 4 C7.2 5.6 6.4 7 4 10.3Z"/></svg><div>4820 Larkspur Ave. | Suite 600<br>Fairhaven, CA 90418</div></div>
    <div>
      <div class="contact-line"><svg viewBox="0 0 8 8"><rect x=".7" y="1.5" width="6.6" height="5"/></svg>dmercer@halloranbrightmoor.com</div>
      <div class="contact-line"><svg viewBox="0 0 8 8"><circle cx="4" cy="4" r="3.3"/></svg>www.halloranbrightmoor.com</div>
      <div class="contact-line"><svg viewBox="0 0 8 8"><path d="M1.2 1.2 2.8.9 3.6 2.6 2.7 3.4C3.2 4.4 3.8 5 4.7 5.4L5.5 4.5 7.1 5.3 6.8 6.9C3.8 7 1 4.3 1.2 1.2Z"/></svg>Tel: (855) 555-0147</div>
    </div>
  </footer>
</section>

<section class="sheet card card-back" aria-label="Business card back">
  <div class="brand brand--light"><span class="brand-square"></span><span>Halloran Brightmoor PC</span></div>
</section>

<section class="sheet envelope" aria-label="Envelope">
  <div class="brand"><span class="brand-square"></span><span>Halloran Brightmoor PC</span></div>
  <footer class="band">4820 Larkspur Ave. | Suite 600, Fairhaven, CA 90418</footer>
</section>

</body>
</html>
```